Book cover design for modern bagpipe music book

This music book will be A4 in size and requires a design for the front and back cover. The focus is on creating a modern and eye catching design, breaking away from the stereotypes of what people think of when they think of bagpipes. Think the OPPOSITE of a bagpiper in a full kilt standing on top of a mountain playing Copper Lanterns Rising!

Book title: Rise Hum March Rest

Other front cover text : Music for the bagpipes by Dermot Fairley

Front cover file ideas uploaded

2 pictures of bagpipes attached.

- The real set of bagpipes give an idea of the correct finer details

- The toy bagpipes perhaps have a better shape with the left 'stick' down

Back cover - No real brief. Keen for it not to be a full block single colour though.

Design requires 3mm bleed for print

Open to ideas and suggestions! Thank you!

```html
<!DOCTYPE html>
<html lang="en">
<head>
<meta charset="utf-8">
<title>Music for the Bagpipes – Dermot Fairley</title>
<link href="https://fonts.googleapis.com/css2?family=Bebas+Neue&display=swap" rel="stylesheet">
<style>
  :root {
    --red: #cf1f2c;
    --black: #000000;
    --white: #ffffff;
    --tile-shadow: rgba(90, 0, 0, 0.35);
    --ghost: rgba(120, 120, 120, 0.28);
  }
  * { margin: 0; padding: 0; box-sizing: border-box; }
  html, body { width: 927px; height: 1200px; overflow: hidden; background: var(--black); }
  .cover {
    position: relative;
    width: 927px;
    height: 1200px;
    background: var(--black);
    overflow: hidden;
    font-family: "Bebas Neue", "Oswald", sans-serif;
  }
  .routine-band {
    position: absolute;
    left: 0; top: 0;
    width: 927px; height: 398px;
    background: var(--red);
  }
  .routine-list {
    position: absolute;
    left: 23px; top: 33px;
    display: flex;
    gap: 21px;
    list-style: none;
  }
  .routine-item { width: 205px; display: flex; flex-direction: column; align-items: center; }
  .routine-tile {
    width: 205px; height: 209px;
    background: var(--white);
    border-radius: 22px;
    box-shadow: 0 4px 6px var(--tile-shadow);
    display: flex; align-items: center; justify-content: center;
  }
  .routine-tile svg { width: 160px; height: 160px; }
  .routine-label {
    margin-top: 46px;
    color: var(--white);
    font-size: 84px;
    line-height: 1;
    letter-spacing: 1px;
    white-space: nowrap;
  }
  .pipe-placeholder {
    width: 110px; height: 150px;
    background: #1a1a1a;
    border-radius: 40% 40% 30% 30%;
  }
  .ghost-instrument {
    position: absolute;
    left: 350px; top: 270px;
    width: 500px; height: 790px;
    background: radial-gradient(ellipse at 40% 55%, var(--ghost) 0%, rgba(120,120,120,0.12) 55%, rgba(0,0,0,0) 75%);
  }
  .title { color: var(--white); font-weight: 400; }
  .title-line {
    position: absolute;
    left: 53px;
    line-height: 1;
    white-space: nowrap;
    transform-origin: left top;
  }
  .title-line-one { top: 589px; font-size: 170px; transform: scaleX(1.08); }
  .title-line-two { top: 743px; font-size: 220px; transform: scaleX(1.2); }
  .byline {
    position: absolute;
    left: 53px; top: 944px;
    color: var(--white);
    font-size: 34px;
    line-height: 1;
  }
  .author {
    position: absolute;
    left: 53px; top: 973px;
    color: var(--red);
    font-size: 193px;
    line-height: 1;
    white-space: nowrap;
    transform: scaleX(0.8);
    transform-origin: left top;
  }
</style>
</head>
<body>
<main class="cover">
  <section class="routine-band">
    <ul class="routine-list">
      <li class="routine-item">
        <div class="routine-tile">
          <svg viewBox="0 0 160 160" aria-hidden="true">
            <g fill="#000">
              <rect x="12" y="30" width="4" height="34"/>
              <rect x="20" y="30" width="4" height="34"/>
              <rect x="28" y="30" width="4" height="34"/>
              <rect x="12" y="60" width="20" height="10" rx="4"/>
              <rect x="18" y="68" width="8" height="62" rx="4"/>
              <circle cx="80" cy="80" r="48"/>
              <path d="M136 30c-10 8-12 30-8 48h6v52h8V30z"/>
            </g>
            <circle cx="80" cy="80" r="40" fill="#fff"/>
            <circle cx="80" cy="80" r="35" fill="#000"/>
          </svg>
        </div>
        <span class="routine-label">Rise</span>
      </li>
      <li class="routine-item">
        <div class="routine-tile">
          <svg viewBox="0 0 160 160" aria-hidden="true">
            <g fill="#000">
              <rect x="8" y="40" width="12" height="90"/>
              <rect x="8" y="102" width="144" height="14"/>
              <rect x="140" y="92" width="12" height="38"/>
              <rect x="26" y="70" width="30" height="18" rx="6"/>
              <rect x="60" y="64" width="86" height="32" rx="6"/>
            </g>
          </svg>
        </div>
        <span class="routine-label">Hum</span>
      </li>
      <li class="routine-item">
        <div class="routine-tile">
          <div class="pipe-placeholder" role="img" aria-label="Small black bagpipe silhouette icon"></div>
        </div>
        <span class="routine-label">March</span>
      </li>
      <li class="routine-item">
        <div class="routine-tile">
          <svg viewBox="0 0 160 160" aria-hidden="true">
            <g fill="none" stroke="#000" stroke-width="14">
              <path d="M38 74a44 44 0 0 1 78-26"/>
              <path d="M122 86a44 44 0 0 1-78 26"/>
            </g>
            <g fill="#000">
              <path d="M100 30l36 0-4 38z"/>
              <path d="M60 130l-36 0 4-38z"/>
            </g>
          </svg>
        </div>
        <span class="routine-label">Rest</span>
      </li>
    </ul>
  </section>

  <div class="ghost-instrument" role="img" aria-label="Large faint grey bagpipe silhouette behind the title"></div>

  <h1 class="title">
    <span class="title-line title-line-one">Music for the</span>
    <span class="title-line title-line-two">Bagpipes</span>
  </h1>
  <p class="byline">By</p>
  <p class="author">Dermot Fairley</p>
</main>
</body>
</html>
```